Unique Elegant Stationary Set

Prepare a unique eye catching stationary set consisting of :
(1) Letterhead
(2) A3 Envelope
(3) Business Card
(4) Email Signature Banner

Package to be elegant, modern, and designers not only to think of design or colors but also materials could make a big difference, embossing, debossing, glossy, matt ....etc.

I attached both our new logos (Stacked or Linear) noting you may use any of them but you cant modify anything in the logos. Also attached our final draft portfolio to see what type of projects we work on and i also have here a glimboard page link showing the direction we want: https://www.glimboard.example/ravelkoton/business-card-design/

Target Market(s)

VVIP / Elite Developers

Industry/Entity Type

Architecture

Font styles to use
Sans Serif
Other font styles liked:
• unitext

Requirements
Should not have
• too many colors, or being busy in general. We want something pleasing to the eye

```html
<!DOCTYPE html>
<html lang="en">
<head>
<meta charset="utf-8">
<title>Corvane Studio — Business Card</title>
<link rel="stylesheet" href="https://fonts.googleapis.com/css2?family=Roboto:wght@300;400;700&display=swap">
<style>
  :root {
    --backdrop: #2b2c2e;
    --paper: #ececec;
    --paper-back: #efefef;
    --brand-red: #d0202b;
    --edge-red: #c8141c;
    --ink-grey: #6f6f6f;
    --ink-soft: #7c7c7c;
    --emboss: #d9d9d9;
  }
  * { box-sizing: border-box; margin: 0; padding: 0; }
  html, body {
    width: 1200px;
    height: 1104px;
    overflow: hidden;
    background: var(--backdrop);
    font-family: "Roboto", Arial, sans-serif;
  }
  .sheet {
    width: 1200px;
    height: 1104px;
    display: flex;
    flex-direction: column;
    align-items: center;
    justify-content: center;
    gap: 44px;
  }
  .card {
    position: relative;
    width: 880px;
    height: 503px;
    background: var(--paper);
    border-bottom: 8px solid var(--edge-red);
    border-right: 3px solid var(--edge-red);
    overflow: hidden;
  }
  .card--back { background: var(--paper-back); }

  /* Front */
  .brand {
    position: absolute;
    left: 78px;
    top: 180px;
    display: flex;
    align-items: center;
    gap: 10px;
    color: var(--brand-red);
    font-weight: 700;
    font-size: 36px;
    line-height: 1;
    letter-spacing: 0.5px;
    text-transform: uppercase;
  }
  .brand__dot {
    width: 10px;
    height: 10px;
    background: var(--brand-red);
  }
  .contact {
    position: absolute;
    left: 500px;
    top: 140px;
    right: 0;
  }
  .contact__topline {
    height: 2px;
    background: var(--brand-red);
    margin-left: 120px;
    margin-bottom: 12px;
  }
  .contact__name {
    color: var(--brand-red);
    font-weight: 700;
    font-size: 24px;
    letter-spacing: 0.3px;
    text-transform: uppercase;
  }
  .contact__role {
    color: var(--ink-grey);
    font-weight: 400;
    font-size: 19px;
    margin-top: 2px;
  }
  .contact__rule {
    width: 220px;
    height: 2px;
    background: var(--brand-red);
    margin: 12px 0 10px 0;
  }
  .contact__list { list-style: none; }
  .contact__item {
    display: flex;
    align-items: center;
    gap: 10px;
    color: var(--ink-grey);
    font-weight: 300;
    font-size: 19px;
    line-height: 30px;
  }
  .contact__icon { width: 15px; height: 15px; flex: none; }
  .address {
    position: absolute;
    left: 300px;
    bottom: 70px;
    color: var(--ink-soft);
    font-style: normal;
    font-weight: 400;
    font-size: 18px;
    line-height: 25px;
  }

  /* Back */
  .back-mark {
    position: absolute;
    inset: 0;
    display: flex;
    align-items: center;
    justify-content: center;
  }
  .back-mark__name {
    color: var(--emboss);
    font-weight: 300;
    font-size: 50px;
    letter-spacing: 14px;
    padding-left: 14px;
    text-transform: uppercase;
    white-space: nowrap;
  }
</style>
</head>
<body>
<main class="sheet">
  <section class="card card--front" aria-label="Business card front">
    <div class="brand"><span class="brand__name">Corvane Studio</span><span class="brand__dot"></span></div>

    <div class="contact">
      <div class="contact__topline"></div>
      <p class="contact__name">Elias Marrow</p>
      <p class="contact__role">Managing Director</p>
      <div class="contact__rule"></div>
      <ul class="contact__list">
        <li class="contact__item">
          <svg class="contact__icon" viewBox="0 0 16 16" aria-hidden="true"><path fill="var(--brand-red)" d="M2 5c0-2 2-3 6-3s6 1 6 3v1h-3V5H5v1H2zM4 7h8l2 6H2z"/></svg>
          044-987 650 321
        </li>
        <li class="contact__item">
          <svg class="contact__icon" viewBox="0 0 16 16" aria-hidden="true"><rect x="1" y="3" width="14" height="10" fill="var(--brand-red)"/><path d="M1 3l7 6 7-6" fill="none" stroke="var(--paper)" stroke-width="1.4"/></svg>
          hello@corvane.example
        </li>
        <li class="contact__item">
          <svg class="contact__icon" viewBox="0 0 16 16" aria-hidden="true"><circle cx="8" cy="8" r="7" fill="var(--brand-red)"/><path d="M1 8h14M8 1c-3 4-3 10 0 14M8 1c3 4 3 10 0 14" fill="none" stroke="var(--paper)" stroke-width="1"/></svg>
          www.corvane.example
        </li>
      </ul>
    </div>

    <address class="address">12 Harlow Lane, Easton<br>Northfield, Zip 4410</address>
  </section>

  <section class="card card--back" aria-label="Business card back">
    <div class="back-mark">
      <span class="back-mark__name">Corvane Studio</span>
    </div>
  </section>
</main>
</body>
</html>
```